Real Estate Flyer (Brenwick Property)

We need a color CMYK high resolution, print quality horizontal real estate property flyer designed in the sizes of 10" wide and 6.7425" tall and another one in 11" wide and 8.5" tall.
Ad should be professionally looking to U.S. standards. It should be sleek, modern yet classy.
We uploaded in Briefs logo files, agent photo, 2 photos of the property (Must use both) and a sample of a flyer for Velmora Grand Luxury Residence. We like how the overlay atop the first photo in the Velmora Grand flyer with the company logo in the overlay. We'd like to incorporate that with our logo, the background color of the overlay should match that of our logo. DON'T CHANGE LOGO COLORS. Only use two colors in ad (exact logo blue color and white). The text in the overlay must be "FOR SALE - Potential Income Producing Commercial Office Building". Other details that should be prominent underneath are "42 Tamber Ln., Schaumburg, IL 60188 - Asking Price: $650,000".
Add "Residential & Commercial" under our company logo in italic font.
Add in flyer: "Located seconds away from the Dunmore Rd. & Hollick Rd. Intersection"
Add in flyer:
- Completely vacant
- 10,000 sq. ft. building
- 55 Car Parking
- 1.38 acre lot
- Over 20 offices and 5 bathrooms.
- Lease out individual office spaces for great monthly cash flow
Put agent's photo and following details professionally displayed:
Pete Glover
Managing Broker
847-555-0143
pete.glover@kqtnrealty.example
Add from Briefs fair housing logo and MLS logo near agent's information. Logos should be small but yet visible to understand text.
Add at bottom of the ad with separation near agent details:
Looking to Buy or Sell?
I’m your one-stop, full service licensed real estate broker.
I deal with all types of real estate properties: Homes, Condos, Townhomes, Multi-Unit Apartment Buildings and Commercial Spaces.
Let My Experience Guide You Through Every Step of the Process!
Fine print:
©2018 KQTN Realty, Inc. All Rights Reserved.

```html
<!DOCTYPE html>
<html lang="en">
<head>
<meta charset="utf-8">
<title>Brenwick Property – For Sale Flyer</title>
<link href="https://fonts.googleapis.com/css2?family=Roboto+Condensed:wght@400;700&family=Nunito+Sans:ital,wght@0,400;0,700;1,400&family=Lobster&display=swap" rel="stylesheet">
<style>
  :root {
    --brand-blue: #1150a5;
    --brand-blue-light: #7d9fd0;
    --white: #ffffff;
    --panel-grey: #f1f1f1;
    --tab-shadow: #e4e4e4;
    --text-grey: #4a4a4a;
    --page-bg: #e6e6e6;
  }
  * { box-sizing: border-box; margin: 0; padding: 0; }
  html, body { width: 1200px; height: 1200px; overflow: hidden; background: var(--page-bg); }
  .flyer {
    position: absolute; left: 175px; top: 50px;
    width: 850px; height: 1100px;
    background: var(--white);
    font-family: "Nunito Sans", sans-serif;
    overflow: hidden;
  }
  .hero-photo {
    position: absolute; left: 0; top: 0; width: 850px; height: 560px;
    background: linear-gradient(180deg, #b9c7d6 0%, #d9cfc0 22%, #c8b79d 45%, #8c7f70 62%, #3f4a5c 78%, #2f5590 100%);
  }
  .hero-overlay { position: absolute; left: 0; top: 0; width: 850px; height: 626px; }

  .sale-tag { position: absolute; left: 266px; top: 0; width: 318px; height: 134px; }
  .sale-tag__shape { position: absolute; left: 0; top: 0; width: 318px; height: 134px; }
  .sale-tag__text {
    position: absolute; left: 30px; top: 17px; width: 258px; height: 84px;
    border-top: 2px solid var(--brand-blue); border-bottom: 2px solid var(--brand-blue);
    font-family: "Roboto Condensed", sans-serif; font-weight: 700;
    font-size: 68px; line-height: 80px; color: var(--brand-blue);
    text-align: center; white-space: nowrap;
  }

  .brand { position: absolute; left: 60px; top: 478px; width: 230px; text-align: center; color: var(--white); }
  .brand__name { font-weight: 700; font-size: 34px; line-height: 40px; display: inline-flex; align-items: center; gap: 8px; white-space: nowrap; }
  .brand__mark { width: 14px; height: 14px; background: var(--white); display: inline-block; }
  .brand__tagline { font-style: italic; font-size: 14px; margin-top: 48px; }
  .hero-divider { position: absolute; left: 337px; top: 469px; width: 2px; height: 123px; background: var(--white); }
  .headline { position: absolute; left: 373px; top: 472px; color: var(--white); font-family: "Roboto Condensed", sans-serif; }
  .headline__title { font-size: 28px; line-height: 41px; }
  .headline__details { font-size: 18px; margin-top: 6px; }

  .location { position: absolute; left: 0; top: 646px; width: 850px; text-align: center; font-family: "Roboto Condensed", sans-serif; font-size: 22px; color: var(--brand-blue); }
  .features { position: absolute; left: 62px; top: 700px; list-style: none; width: 340px; }
  .features li { position: relative; padding-left: 39px; font-size: 18.5px; line-height: 33.3px; color: var(--text-grey); }
  .features svg { position: absolute; left: 0; top: 10px; width: 18px; height: 14px; }
  .pitch { position: absolute; left: 420px; top: 690px; width: 359px; height: 249px; background: var(--panel-grey); padding: 12px 18px; }
  .pitch__title { font-family: "Lobster", cursive; font-size: 22px; color: var(--brand-blue); margin-bottom: 6px; font-weight: 400; }
  .pitch p { font-size: 15.5px; line-height: 23.7px; color: var(--text-grey); }

  .agent-bar { position: absolute; left: 0; top: 981px; width: 850px; height: 119px; background: var(--brand-blue); }
  .agent-photo { position: absolute; left: 64px; top: 961px; width: 93px; height: 121px; border: 3px solid var(--white); background: linear-gradient(180deg, #d8d8d8 0%, #b9a99a 50%, #2c2f36 100%); }
  .agent-info { color: var(--white); }
  .agent-name { position: absolute; left: 192px; top: 1000px; font-weight: 700; font-size: 19px; }
  .agent-role { position: absolute; left: 192px; top: 1025px; font-size: 16px; }
  .contact { position: absolute; left: 343px; font-size: 15px; display: flex; align-items: center; gap: 8px; white-space: nowrap; }
  .contact svg { width: 14px; height: 14px; flex: none; }
  .contact--phone { top: 1001px; }
  .contact--email { top: 1026px; }
  .fine-print { position: absolute; left: 192px; top: 1059px; font-size: 14.5px; }
  .fine-rule { position: absolute; left: 514px; top: 1070px; width: 336px; height: 1px; background: var(--white); }
  .badge { position: absolute; border: 2px solid var(--white); }
  .badge--listing { left: 618px; top: 1001px; width: 92px; height: 44px; }
  .badge--housing { left: 734px; top: 1001px; width: 40px; height: 44px; border-radius: 4px; }
</style>
</head>
<body>
<main class="flyer">
  <div class="hero-photo" role="img" aria-label="Photograph of the two-storey white office building with dormer windows, trees and parking lot at sunset"></div>
  <svg class="hero-overlay" viewBox="0 0 850 626" aria-hidden="true">
    <polygon points="0,550 850,412 850,618 0,618" fill="var(--brand-blue)"/>
    <rect x="0" y="618" width="850" height="8" fill="var(--brand-blue-light)"/>
  </svg>

  <div class="sale-tag">
    <svg class="sale-tag__shape" viewBox="0 0 318 134" aria-hidden="true">
      <polygon points="0,0 318,0 318,112 159,134 0,112" fill="var(--tab-shadow)"/>
      <polygon points="0,0 318,0 318,112 159,124 0,112" fill="var(--white)"/>
    </svg>
    <div class="sale-tag__text">FOR SALE</div>
  </div>

  <div class="brand">
    <div class="brand__name"><span class="brand__mark"></span>KQTN Realty</div>
    <div class="brand__tagline">Residential &amp; Commercial</div>
  </div>
  <div class="hero-divider"></div>
  <div class="headline">
    <div class="headline__title">Potential Income Producing Commercial<br>Office Building</div>
    <div class="headline__details">42 Tamber Ln., Schaumburg, IL 60188 Asking Price: $650,000</div>
  </div>

  <div class="location">Located seconds away from the Dunmore Rd. &amp; Hollick Rd. Intersection</div>

  <ul class="features">
    <li><svg viewBox="0 0 18 14"><path d="M1 7 L6.5 12 L17 2" stroke="var(--brand-blue)" stroke-width="3.5" fill="none"/></svg>Completely vacant</li>
    <li><svg viewBox="0 0 18 14"><path d="M1 7 L6.5 12 L17 2" stroke="var(--brand-blue)" stroke-width="3.5" fill="none"/></svg>10,000 sq. ft. building</li>
    <li><svg viewBox="0 0 18 14"><path d="M1 7 L6.5 12 L17 2" stroke="var(--brand-blue)" stroke-width="3.5" fill="none"/></svg>55 Car Parking</li>
    <li><svg viewBox="0 0 18 14"><path d="M1 7 L6.5 12 L17 2" stroke="var(--brand-blue)" stroke-width="3.5" fill="none"/></svg>1.38 acre lot</li>
    <li><svg viewBox="0 0 18 14"><path d="M1 7 L6.5 12 L17 2" stroke="var(--brand-blue)" stroke-width="3.5" fill="none"/></svg>Over 20 offices and 5 bathrooms.</li>
    <li><svg viewBox="0 0 18 14"><path d="M1 7 L6.5 12 L17 2" stroke="var(--brand-blue)" stroke-width="3.5" fill="none"/></svg>Lease out individual office spaces for great monthly cash flow</li>
  </ul>

  <section class="pitch">
    <h2 class="pitch__title">Looking to Buy or Sell?</h2>
    <p>I’m your one-stop, full service licensed real estate broker.<br>I deal with all types of real estate properties: Homes, Condos, Townhomes, Multi-Unit Apartment Buildings and Commercial Spaces.<br>Let My Experience Guide You Through Every Step of the Process!</p>
  </section>

  <div class="agent-bar"></div>
  <div class="agent-photo" role="img" aria-label="Portrait photo of the managing broker"></div>
  <div class="agent-info">
    <div class="agent-name">Pete Glover</div>
    <div class="agent-role">Managing Broker</div>
    <div class="contact contact--phone">
      <svg viewBox="0 0 14 14"><path d="M3 1 L5 4 L4 5.5 C5 7.5 6.5 9 8.5 10 L10 9 L13 11 L11.5 13 C6 12.5 1.5 8 1 2.5 Z" fill="none" stroke="var(--white)" stroke-width="1.1"/></svg>
      <span>847-555-0143</span>
    </div>
    <div class="contact contact--email">
      <svg viewBox="0 0 14 14"><rect x="1" y="3" width="12" height="8.5" fill="none" stroke="var(--white)" stroke-width="1.1"/><path d="M1 3 L7 8 L13 3" fill="none" stroke="var(--white)" stroke-width="1.1"/></svg>
      <span>pete.glover@kqtnrealty.example</span>
    </div>
    <div class="fine-print">©2018 KQTN Realty, Inc. All Rights Reserved.</div>
  </div>
  <div class="fine-rule"></div>
  <div class="badge badge--listing" role="img" aria-label="Listing service badge"></div>
  <div class="badge badge--housing" role="img" aria-label="Fair housing badge"></div>
</main>
</body>
</html>
```